One of a kind service business!

We are the only ocean freight auditing company in the entire world that does what we do. We provide a innovative service in auditing our clients invoices for billing errors as it relates to the import and export of their products anywhere in the world. We'd like to retain the current logo - but we are open to any interesting concepts that can complete the card.

Target Market(s)

C-Level and Senior Financial executives

Industry/Entity Type

Auditing

Requirements
Must have

• ONE SIDED ONLY
Should not have
• no cartoonish images

```html
<!DOCTYPE html>
<html lang="en">
<head>
<meta charset="utf-8">
<title>Tideway Audit – Business Card</title>
<link href="https://fonts.googleapis.com/css2?family=Russo+One&display=swap" rel="stylesheet">
<style>
  :root {
    --page-bg: #ffffff;
    --sky-top: #63bbe0;
    --sky-mid: #67bde2;
    --sky-bottom: #a9d9ef;
    --sea-top: #3fb3df;
    --sea-bottom: #03a2d4;
    --navy: #002d62;
  }
  html, body {
    margin: 0;
    padding: 0;
    width: 1200px;
    height: 900px;
    overflow: hidden;
    background: var(--page-bg);
  }
  .canvas {
    position: relative;
    width: 1200px;
    height: 900px;
  }
  .card {
    position: absolute;
    left: 238px;
    top: 249px;
    width: 723px;
    height: 402px;
  }
  .card-art {
    position: absolute;
    inset: 0;
    width: 100%;
    height: 100%;
  }
  .contact {
    position: absolute;
    left: 42px;
    top: 127px;
    margin: 0;
    padding: 0;
    list-style: none;
    font-family: "Russo One", sans-serif;
    font-size: 20px;
    color: var(--navy);
    letter-spacing: 0.5px;
  }
  .contact li {
    height: 39px;
    line-height: 39px;
  }
  .brand-name {
    position: absolute;
    left: 440px;
    top: 110px;
    width: 250px;
    text-align: center;
    font-family: "Russo One", sans-serif;
    font-size: 36px;
    line-height: 1.1;
    color: var(--navy);
    margin: 0;
  }
</style>
</head>
<body>
<main class="canvas">
  <section class="card">
    <svg class="card-art" viewBox="0 0 723 402" aria-hidden="true">
      <defs>
        <linearGradient id="sky" x1="0" y1="0" x2="0" y2="1">
          <stop offset="0" stop-color="var(--sky-top)"/>
          <stop offset="0.55" stop-color="var(--sky-mid)"/>
          <stop offset="1" stop-color="var(--sky-bottom)"/>
        </linearGradient>
        <linearGradient id="sea" x1="0" y1="0" x2="0" y2="1">
          <stop offset="0" stop-color="var(--sea-top)"/>
          <stop offset="1" stop-color="var(--sea-bottom)"/>
        </linearGradient>
      </defs>
      <path class="sky-panel" d="M0,0 H723 V306 Q430,322 0,280 Z" fill="url(#sky)"/>
      <path class="sea-band" d="M0,320 Q430,362 723,345 V402 H0 Z" fill="url(#sea)"/>
    </svg>
    <ul class="contact">
      <li class="contact-name">Marten Olsby</li>
      <li class="contact-email">hello@tidewayaudit.com</li>
      <li class="contact-phone">0144 20583716</li>
    </ul>
    <p class="brand-name">Tideway Audit</p>
  </section>
</main>
</body>
</html>
```